We need a full website with logo/graphics/woocommerce for hemp-based company

This site will be lunavetta.com. It is a website featuring the fact we are the only manufacturer to produce CBDP and THCP. It should be great on mobile and desktop. We will pay for any extensions needed and while it should be a simple site:

About Us
About the Laboratory
About CBDP
About THCP
Shop
Contact Us

Only 4 products on the site.

It can be wordpress or joomla. Your choice. You must install the final website on our server. We agree to pay for monthly support that must be submitted in your quote.

He have a great graphics designer that will assist keeping colors and graphics clean according to your specifications.

Industry/Entity Type

Hemp CBD THC

Coding

Coded - Design and coding required

Number of Pages Required

5+ page

Requirements
Must have
• A simple clean layout

```html
<!DOCTYPE html>
<html lang="en">
<head>
<meta charset="utf-8">
<title>Lunavetta — TCHP and CBDP in bulk batches</title>
<link href="https://fonts.googleapis.com/css2?family=Poppins:wght@300;400;500;600;700&display=swap" rel="stylesheet">
<style>
:root{
  --green:#8cc63f;
  --green-soft:#b7dd93;
  --green-pale:#eef6e6;
  --teal:#3a9fae;
  --ink:#3a3f47;
  --text:#777c83;
  --footer:#1f2533;
  --white:#ffffff;
  --line:#c9e4ad;
}
*{margin:0;padding:0;box-sizing:border-box}
html,body{width:1200px;height:4566px;overflow:hidden}
body{font-family:'Poppins',sans-serif;color:var(--text);background:var(--white);position:relative}
.abs{position:absolute}
.btn{position:absolute;display:flex;align-items:center;justify-content:center;border-radius:24px;
  background:linear-gradient(90deg,var(--green),var(--teal));color:var(--white);font-size:12.5px;font-weight:600;letter-spacing:.3px;text-transform:uppercase}
.h2{position:absolute;font-size:33px;font-weight:600;color:var(--ink);line-height:1.2}
.para{position:absolute;font-size:12.2px;line-height:26px;color:var(--text)}
.center{text-align:center}
.photo{position:absolute;border-radius:50%}
.ring{position:absolute;border-radius:50%;border:1.5px solid var(--line)}
.dot{position:absolute;border-radius:50%;background:var(--green)}
.dot.soft{background:var(--green-soft);opacity:.8}
.icon-badge{position:absolute;width:104px;height:104px;border-radius:50%;background:var(--green);display:flex;align-items:center;justify-content:center}
.brand{font-weight:700;color:var(--green);letter-spacing:.5px}
/* nav */
.nav{position:absolute;top:49px;right:60px;display:flex;gap:32px;font-size:12.5px;font-weight:500;color:var(--ink);text-transform:uppercase}
.nav .active{color:var(--teal)}
/* products */
.card{position:absolute;top:3236px;width:247px;height:336px;border:1.5px solid #e6e9ec;border-radius:4px;background:var(--white);text-align:center}
.card .bottle{position:absolute;left:80px;top:22px;width:86px;height:230px;border-radius:10px;background:linear-gradient(180deg,#2a2d31,#141618)}
.card .name{position:absolute;top:266px;width:100%;font-size:16px;font-weight:600;color:var(--ink)}
.card .price{position:absolute;top:292px;width:100%;font-size:12.5px;color:var(--green)}
/* contact */
.field{position:absolute;border:1.5px solid rgba(255,255,255,.55);background:rgba(255,255,255,.15);border-radius:3px;color:var(--white);font-size:12px;padding:11px 12px}
/* footer */
.foot-links{position:absolute;left:339px;top:4341px;font-size:12.5px;line-height:24px;color:var(--white)}
.foot-links .active{color:var(--green)}
.foot-text{position:absolute;font-size:12.5px;line-height:24px;color:var(--white)}
</style>
</head>
<body>

<!-- Header -->
<header>
  <div class="abs" style="left:62px;top:18px;width:94px;text-align:center">
    <div style="width:34px;height:34px;border-radius:50%;background:var(--green);margin:0 auto 10px"></div>
    <div class="brand" style="font-size:15px">LUNAVETTA</div>
  </div>
  <nav class="nav">
    <span class="active">Home</span><span>About</span><span>The Laboratory</span><span>CBDP</span><span>THCP</span><span>Shop</span><span>Contact Us</span>
  </nav>
</header>

<!-- Hero -->
<section class="hero">
  <h1 class="abs" style="left:62px;top:262px;font-size:42px;line-height:50px;font-weight:700;color:var(--ink)">TCHP and CBDP<br>in bulk batches.</h1>
  <p class="abs" style="left:62px;top:370px;font-size:13px;line-height:23px;color:var(--text)">Lunavetta is the first lab to be able to make the minor<br>cannabinoids TCHP and CBDP in bulk batches.</p>
  <div class="btn" style="left:60px;top:434px;width:158px;height:45px">Order Now</div>

  <div class="ring" style="left:512px;top:88px;width:724px;height:724px"></div>
  <div class="photo" role="img" aria-label="Close-up of green hemp leaves" style="left:603px;top:156px;width:602px;height:602px;background:radial-gradient(circle at 45% 40%,#4c9a3a,#1d4d26 70%,#0f2a18)"></div>
  <div class="photo" role="img" aria-label="Woman holding a hemp leaf beside a dropper bottle" style="left:1007px;top:85px;width:184px;height:184px;background:linear-gradient(135deg,#e9d3c4,#c89c82);border:4px solid var(--white)"></div>
  <div class="photo" role="img" aria-label="Lab technician filling test tubes with oil" style="left:515px;top:520px;width:300px;height:300px;background:linear-gradient(135deg,#e5eef2,#a9bfca);border:5px solid var(--white)"></div>
  <div class="dot" style="left:1032px;top:78px;width:38px;height:38px"></div>
  <div class="dot soft" style="left:585px;top:478px;width:66px;height:66px"></div>
  <div class="dot" style="left:880px;top:748px;width:38px;height:38px"></div>
  <div class="dot soft" style="left:1090px;top:765px;width:66px;height:66px"></div>

  <div class="abs" role="img" aria-label="Line drawing of a cannabinoid molecule structure" style="left:60px;top:615px;width:600px;height:330px;background:linear-gradient(90deg,rgba(140,198,63,.08),rgba(140,198,63,.02));border-radius:8px"></div>
</section>

<!-- About -->
<section class="about">
  <div class="abs" style="left:0;top:1028px;width:1200px;height:346px;background:linear-gradient(180deg,var(--white),var(--green-pale))"></div>
  <svg class="abs" style="left:0;top:1290px" width="1200" height="120" viewBox="0 0 1200 120" preserveAspectRatio="none">
    <path d="M0 75 C250 20 450 20 650 60 C850 100 1050 80 1200 35 L1200 120 L0 120 Z" fill="#ffffff"/>
  </svg>
  <h2 class="h2 center" style="left:0;top:999px;width:1200px">About Lunavetta</h2>
  <p class="para center" style="left:280px;top:1055px;width:640px">Lorem Ipsum is simply dummy text of the printing and typesetting industry. Lorem Ipsum has been the industry's standard dummy text ever since the 1500s, when an unknown printer took a galley of type and scrambled it to make a type specimen book. It has survived not only five centuries, but also the leap into electronic typesetting, remaining essentially unchanged.</p>
  <div class="btn" style="left:528px;top:1191px;width:144px;height:44px">Read More</div>
</section>

<!-- Laboratory -->
<section>
  <div class="ring" style="left:130px;top:1463px;width:414px;height:414px"></div>
  <div class="photo" role="img" aria-label="Scientist examining a hemp seedling with a dropper" style="left:157px;top:1490px;width:360px;height:360px;background:radial-gradient(circle at 50% 45%,#9fb3c2,#4d6478 75%)"></div>
  <div class="dot soft" style="left:168px;top:1488px;width:66px;height:66px"></div>
  <div class="dot" style="left:200px;top:1822px;width:36px;height:36px"></div>
  <div class="icon-badge" style="left:430px;top:1490px">
    <svg width="46" height="46" viewBox="0 0 46 46" fill="none" stroke="#fff" stroke-width="2" stroke-linejoin="round"><path d="M14 6h10M17 6v12L7 38h24L21 18V6"/><path d="M12 30h14"/><rect x="32" y="10" width="8" height="28" rx="4"/></svg>
  </div>
  <h2 class="h2" style="left:624px;top:1504px">About The Laboratory</h2>
  <p class="para" style="left:624px;top:1556px;width:445px">Lorem Ipsum is simply dummy text of the printing and typesetting industry. Lorem Ipsum has been the industry's standard dummy text ever since the 1500s, when an unknown printer took a galley of type and scrambled it to make a type specimen book. It has survived not only five centuries, but also the leap into electronic typesetting, remaining essentially unchanged.</p>
  <div class="btn" style="left:622px;top:1751px;width:143px;height:45px">Read More</div>
</section>

<!-- CBD -->
<section>
  <h2 class="h2" style="left:92px;top:2024px">About CBDP</h2>
  <p class="para" style="left:92px;top:2077px;width:445px">Lorem Ipsum is simply dummy text of the printing and typesetting industry. Lorem Ipsum has been the industry's standard dummy text ever since the 1500s, when an unknown printer took a galley of type and scrambled it to make a type specimen book. It has survived not only five centuries, but also the leap into electronic typesetting, remaining essentially unchanged.</p>
  <div class="btn" style="left:90px;top:2272px;width:143px;height:43px">Read More</div>
  <div class="ring" style="left:656px;top:1962px;width:414px;height:414px"></div>
  <div class="photo" role="img" aria-label="Top view of a flowering hemp plant" style="left:685px;top:1991px;width:360px;height:360px;background:radial-gradient(circle at 50% 50%,#6f9c48,#2c4a2a 75%)"></div>
  <div class="dot soft" style="left:978px;top:2006px;width:64px;height:64px"></div>
  <div class="dot" style="left:984px;top:2312px;width:36px;height:36px"></div>
  <div class="icon-badge" style="left:652px;top:1992px">
    <svg width="44" height="44" viewBox="0 0 44 44" fill="none" stroke="#fff" stroke-width="1.8" stroke-linejoin="round"><path d="M22 6c3 7 3 15 0 24-3-9-3-17 0-24zM22 30C16 24 10 20 6 18c3 6 9 10 16 12zM22 30c6-6 12-10 16-12-3 6-9 10-16 12zM22 30v8"/></svg>
  </div>
  <div class="abs" role="img" aria-label="Line drawing of a cannabinoid molecule structure" style="left:575px;top:2255px;width:240px;height:128px;background:rgba(140,198,63,.06);border-radius:6px"></div>
</section>

<!-- THCP -->
<section>
  <div class="ring" style="left:130px;top:2468px;width:414px;height:414px"></div>
  <div class="photo" role="img" aria-label="Amber cannabinoid crystals lifted from a glass jar" style="left:157px;top:2496px;width:360px;height:360px;background:radial-gradient(circle at 50% 45%,#c98e2e,#4e3a22 60%,#1e2536)"></div>
  <div class="dot soft" style="left:168px;top:2494px;width:66px;height:66px"></div>
  <div class="dot" style="left:118px;top:2718px;width:38px;height:38px"></div>
  <div class="icon-badge" style="left:430px;top:2496px">
    <svg width="44" height="44" viewBox="0 0 44 44" fill="none" stroke="#fff" stroke-width="2" stroke-linejoin="round"><rect x="22" y="16" width="14" height="22" rx="3"/><path d="M25 16v-5h8v5M29 22v10M24 27h10"/><path d="M8 10l8 14M12 26a3 3 0 1 0 4-2"/></svg>
  </div>
  <h2 class="h2" style="left:624px;top:2532px">About THCP</h2>
  <p class="para" style="left:624px;top:2584px;width:445px">Lorem Ipsum is simply dummy text of the printing and typesetting industry. Lorem Ipsum has been the industry's standard dummy text ever since the 1500s, when an unknown printer took a galley of type and scrambled it to make a type specimen book. It has survived not only five centuries, but also the leap into electronic typesetting, remaining essentially unchanged.</p>
  <div class="btn" style="left:622px;top:2780px;width:143px;height:44px">Read More</div>
  <div class="abs" role="img" aria-label="Line drawing of a cannabinoid molecule structure" style="left:428px;top:2770px;width:225px;height:128px;background:rgba(140,198,63,.06);border-radius:6px"></div>
</section>

<!-- Products -->
<section>
  <svg class="abs" style="left:0;top:2950px" width="1200" height="280" viewBox="0 0 1200 280" preserveAspectRatio="none">
    <defs><linearGradient id="prodBg" x1="0" y1="0" x2="0" y2="1"><stop offset="0" stop-color="#eef6e6"/><stop offset="1" stop-color="#ffffff"/></linearGradient></defs>
    <path d="M0 60 C200 10 400 10 600 40 C800 70 1000 30 1200 10 L1200 280 L0 280 Z" fill="url(#prodBg)"/>
  </svg>
  <h2 class="h2 center" style="left:0;top:3085px;width:1200px">Our Products</h2>
  <p class="para center" style="left:280px;top:3138px;width:640px">Lorem Ipsum is simply dummy text of the printing and typesetting industry. Lorem Ipsum has been the industry's standard dummy text ever since the 1500s.</p>
  <div class="card" style="left:60px"><div class="bottle" role="img" aria-label="Dropper bottle of oil"></div><div class="name">Product Name</div><div class="price">$ 20.00</div></div>
  <div class="card" style="left:337px"><div class="bottle" role="img" aria-label="Dropper bottle of oil"></div><div class="name">Product Name</div><div class="price">$ 20.00</div></div>
  <div class="card" style="left:615px"><div class="bottle" role="img" aria-label="Dropper bottle of oil"></div><div class="name">Product Name</div><div class="price">$ 20.00</div></div>
  <div class="card" style="left:892px"><div class="bottle" role="img" aria-label="Dropper bottle of oil"></div><div class="name">Product Name</div><div class="price">$ 20.00</div></div>
</section>

<!-- Contact -->
<section>
  <svg class="abs" style="left:0;top:3625px" width="1200" height="700" viewBox="0 0 1200 700" preserveAspectRatio="none" role="img" aria-label="Hemp leaves background in green and teal">
    <defs><linearGradient id="contactBg" x1="0" y1="0" x2="1" y2="1"><stop offset="0" stop-color="#5ea93a"/><stop offset=".55" stop-color="#6fb83f"/><stop offset="1" stop-color="#2f8e9c"/></linearGradient></defs>
    <path d="M0 0 C300 90 600 120 900 80 C1050 60 1150 30 1200 10 L1200 700 L0 700 Z" fill="url(#contactBg)"/>
  </svg>
  <h2 class="h2 center" style="left:0;top:3791px;width:1200px;color:var(--white)">Contact Us</h2>
  <p class="para center" style="left:280px;top:3834px;width:640px;color:var(--white)">Lorem ipsum is simply dummy text of the printing and typesetting industry. Lorem Ipsum has been the industry's standard dummy text ever since the 1500.</p>
  <div class="field" style="left:292px;top:3896px;width:300px;height:44px">Name</div>
  <div class="field" style="left:608px;top:3896px;width:300px;height:44px">Contact No.</div>
  <div class="field" style="left:292px;top:3955px;width:616px;height:44px">Email</div>
  <div class="field" style="left:292px;top:4015px;width:616px;height:88px">Message</div>
</section>

<!-- Footer -->
<footer>
  <svg class="abs" style="left:0;top:4240px" width="1200" height="326" viewBox="0 0 1200 326" preserveAspectRatio="none">
    <path d="M0 50 C300 0 800 -10 1200 55 L1200 326 L0 326 Z" fill="#1f2533"/>
  </svg>
  <div class="abs" style="left:125px;top:4344px;width:116px;text-align:center">
    <div style="width:34px;height:34px;border-radius:50%;background:var(--green);margin:0 auto 10px"></div>
    <div class="brand" style="font-size:15px">LUNAVETTA</div>
  </div>
  <div class="foot-text" style="left:62px;top:4446px;font-size:11.5px">© LUNAVETTA - 2021. All Rights Reserved.</div>
  <div class="abs" style="left:119px;top:4484px;width:32px;height:32px;border-radius:50%;background:var(--green)"></div>
  <div class="abs" style="left:163px;top:4484px;width:32px;height:32px;border-radius:50%;border:1.5px solid var(--green)"></div>
  <div class="abs" style="left:209px;top:4484px;width:32px;height:32px;border-radius:50%;border:1.5px solid var(--green)"></div>

  <div class="foot-links"><span class="active">Home</span><br>About<br>The Laboratory<br>CBDP<br>THCP<br>Shop<br>Contact Us</div>

  <svg class="abs" style="left:612px;top:4344px" width="14" height="16" viewBox="0 0 14 16" fill="var(--green)"><path d="M7 0a6 6 0 0 0-6 6c0 4.5 6 10 6 10s6-5.5 6-10a6 6 0 0 0-6-6zm0 8.5A2.5 2.5 0 1 1 7 3.5a2.5 2.5 0 0 1 0 5z"/></svg>
  <div class="foot-text" style="left:638px;top:4338px">Lorem ipsum is simply dummy text<br>and printing typesetting.</div>
  <svg class="abs" style="left:612px;top:4410px" width="15" height="15" viewBox="0 0 24 24" fill="var(--green)"><path d="M6.6 10.8a15.1 15.1 0 0 0 6.6 6.6l2.2-2.2a1 1 0 0 1 1-.25 11.4 11.4 0 0 0 3.6.57 1 1 0 0 1 1 1V20a1 1 0 0 1-1 1A17 17 0 0 1 3 4a1 1 0 0 1 1-1h3.5a1 1 0 0 1 1 1c0 1.25.2 2.45.57 3.57a1 1 0 0 1-.25 1z"/></svg>
  <div class="foot-text" style="left:638px;top:4405px">123 4567890</div>
  <svg class="abs" style="left:612px;top:4453px" width="16" height="12" viewBox="0 0 16 12" fill="var(--green)"><path d="M0 0h16v12H0z" opacity=".0"/><path d="M0 0h16v1.5L8 7 0 1.5zM0 3.3l8 5.4 8-5.4V12H0z"/></svg>
  <div class="foot-text" style="left:638px;top:4447px">info@lunavetta.com</div>

  <div class="foot-text" style="left:893px;top:4338px">Subscribe to stay with us and update<br>our news, offers and etc...</div>
  <div class="abs" style="left:892px;top:4401px;width:246px;height:37px;background:var(--white);border-radius:3px;font-size:11.5px;color:#999;padding:10px 12px">Enter email here...</div>
  <div class="btn" style="left:893px;top:4452px;width:142px;height:41px">Subscribe</div>
</footer>

</body>
</html>
```